Notary Signing Agent Need Business card Design

Need a Business card design for my new company. RT Belvoni-Strand LLC
Mobile Notary Signing Agent. I go to the customer for closing of Mortgage's Documents . possible signs of honesty, integrity and confidentiality.

Work with Title company to Notary Mortgage closing.

My Target Market is Title companies. Banks and Financial Institution.

Color Blue to Black Professional ) if needed some Green Little Red

And possible a company logo.

Mobile ( travel to clients ) Integrity, Honest Trustworthy. A show of Professional services.

Would like company name and my name on card

Use both sides and front with business name and my name. phone numbers.

Target Market(s)

Title company, Banks mortgage company

Industry/Entity Type

Travel

Contact Information for Business Card

Notary, Certified signing agent, Mobile

Colors
0455a3

Requirements
Must have
• Name of company , owners name phone number,
Nice to have
• blue and black color like a professional look but not limit to these only.
• a stand out from other cards .

```html
<!DOCTYPE html>
<html lang="en">
<head>
<meta charset="utf-8">
<title>RT Belvoni-Strand LLC – Business Card</title>
<link rel="stylesheet" href="https://fonts.googleapis.com/css2?family=Oxanium:wght@400;500&display=swap">
<style>
  :root {
    --page-bg: #f2f3f4;
    --card-black: #121314;
    --card-black-soft: #1c1e20;
    --teal: #13b5b0;
    --edge-gold: #c8c24a;
    --divider-blue: #1e9ad6;
    --text-teal: #17bdb7;
  }
  * { margin: 0; padding: 0; box-sizing: border-box; }
  html, body {
    width: 1200px; height: 800px; overflow: hidden;
    background: var(--page-bg);
    font-family: "Oxanium", sans-serif;
  }
  .sheet {
    width: 1200px; height: 800px;
    display: flex; align-items: center; justify-content: center; gap: 60px;
  }
  .card {
    position: relative;
    width: 525px; height: 300px;
    border-radius: 22px;
    overflow: hidden;
    background: radial-gradient(ellipse at 50% 40%, var(--card-black-soft), var(--card-black) 75%);
    box-shadow: 0 10px 28px rgba(0,0,0,.25);
  }
  .card-accents { position: absolute; inset: 0; width: 100%; height: 100%; }
  .company-name {
    color: var(--text-teal);
    font-weight: 500;
    letter-spacing: .02em;
    line-height: 1.1;
  }
  /* front */
  .card-front .brand {
    position: absolute; left: 50px; top: 0; width: 190px; height: 300px;
    display: flex; align-items: center; justify-content: center; text-align: center;
  }
  .card-front .company-name { font-size: 22px; }
  .card-front .divider {
    position: absolute; left: 262px; top: 60px; width: 2px; height: 160px;
    background: var(--divider-blue);
  }
  .contact {
    position: absolute; left: 290px; top: 72px;
    color: var(--text-teal);
    letter-spacing: .2em;
  }
  .contact-name { font-size: 20px; font-weight: 500; text-transform: uppercase; margin-bottom: 12px; }
  .contact-line { display: flex; align-items: center; gap: 10px; font-size: 17px; margin-bottom: 6px; }
  .contact-line svg { width: 14px; height: 16px; flex: none; }
  /* back */
  .card-back .brand {
    position: absolute; inset: 0;
    display: flex; align-items: center; justify-content: center;
  }
  .card-back .company-name { font-size: 34px; }
</style>
</head>
<body>
<main class="sheet">

  <section class="card card-front" aria-label="Business card front">
    <svg class="card-accents" viewBox="0 0 525 300" aria-hidden="true">
      <polygon points="0,0 28,0 0,165" fill="var(--teal)"/>
      <line x1="28" y1="0" x2="0" y2="165" stroke="var(--edge-gold)" stroke-width="1.5"/>
      <polygon points="470,300 525,300 525,110" fill="var(--teal)"/>
      <line x1="470" y1="300" x2="525" y2="110" stroke="var(--edge-gold)" stroke-width="1.5"/>
    </svg>
    <div class="brand"><p class="company-name">RT Belvoni-Strand LLC</p></div>
    <div class="divider"></div>
    <div class="contact">
      <p class="contact-name">Daniel R Hollis</p>
      <p class="contact-line">
        <svg viewBox="0 0 14 16" aria-hidden="true"><rect x="1.5" y="1.5" width="11" height="13" rx="1.5" fill="none" stroke="currentColor" stroke-width="1.5"/></svg>
        555-014-2263
      </p>
      <p class="contact-line">
        <svg viewBox="0 0 14 16" aria-hidden="true"><rect x="3" y="1" width="8" height="14" rx="1.5" fill="currentColor"/><rect x="4.5" y="3" width="5" height="7" fill="var(--card-black)"/></svg>
        555-017-3391
      </p>
    </div>
  </section>

  <section class="card card-back" aria-label="Business card back">
    <svg class="card-accents" viewBox="0 0 525 300" aria-hidden="true">
      <polygon points="400,0 525,0 525,140" fill="var(--teal)"/>
      <line x1="400" y1="0" x2="525" y2="140" stroke="var(--edge-gold)" stroke-width="1.5"/>
    </svg>
    <div class="brand"><p class="company-name">RT Belvoni-Strand LLC</p></div>
  </section>

</main>
</body>
</html>
```